Harbor Nightclub

Nightclub flyer., digital single sided, for KV and PX. I included samples of some previous flyers we've used. Sample Info:
HARBOR
FRIDAYS
FRI MAY 1 2020
DJ VORTAN (club floor)
DJ RUZO & DJ TAV (residents on the lounge floor)
4217 Marlow Avenue Sacramento
www.harborvenuehall.example for list/VIP inquiries

Target Market(s)

Upscale top 40 crowd but want some cool and artsy like the examples included.

Font styles to use
Sans Serif

Requirements
Must have
• Harbor Logo
Nice to have
• Would be nice if the flyer can be incorporated later with DJ photos (sometimes we will add dj photos to pixagram etc). Would like a big city type of feel.
Should not have
• Nothing too sexual.

```html
<!DOCTYPE html>
<html lang="en">
<head>
<meta charset="utf-8">
<title>Harbor Fridays – Flyer</title>
<link href="https://fonts.googleapis.com/css2?family=Montserrat:ital,wght@0,300;0,500;0,600;0,700;1,800&family=Barlow+Semi+Condensed:wght@500;600&display=swap" rel="stylesheet">
<style>
  :root {
    --page: #f2f2f4;
    --night-deep: #150a3c;
    --night-mid: #3a0f6e;
    --violet: #7a1fd6;
    --violet-bright: #a43cff;
    --magenta: #c0267f;
    --cyan: #2fb8e6;
    --amber: #e09a3a;
    --orange-line: #e2552a;
    --ink: #ffffff;
    --ink-soft: #e6dcff;
    --venue-dot: #b7a863;
  }
  * { margin: 0; padding: 0; box-sizing: border-box; }
  html, body { width: 1200px; height: 830px; overflow: hidden; }
  body { background: var(--page); position: relative; font-family: "Montserrat", sans-serif; }

  .flyer {
    position: absolute; left: 324px; top: 25px;
    width: 552px; height: 780px; overflow: hidden;
    background:
      radial-gradient(ellipse 60% 40% at 50% 35%, rgba(122,31,214,.45), transparent 70%),
      linear-gradient(160deg, var(--magenta) 0%, var(--night-mid) 18%, var(--night-deep) 45%, var(--night-mid) 75%, #5a1a8c 100%);
    box-shadow: 0 6px 24px rgba(0,0,0,.18);
    color: var(--ink);
  }
  .backdrop { position: absolute; inset: 0; width: 100%; height: 100%; }

  .level-glow {
    position: absolute; width: 70px; border-radius: 4px;
    background: linear-gradient(90deg, rgba(47,184,230,.35), rgba(224,74,138,.35), rgba(224,154,58,.35));
  }
  .level-glow--top { top: 26px; height: 150px;
    -webkit-mask-image: linear-gradient(to bottom, #000 30%, transparent);
    mask-image: linear-gradient(to bottom, #000 30%, transparent); }
  .level-glow--bottom { top: 630px; height: 130px;
    -webkit-mask-image: linear-gradient(to top, #000 30%, transparent);
    mask-image: linear-gradient(to top, #000 30%, transparent); }
  .level-glow--left { left: 22px; }
  .level-glow--right { left: 460px; transform: scaleX(-1); }

  .event-title { font-weight: 800; }
  .badge-title {
    position: absolute; left: 0; width: 580px; text-align: center;
    font-style: italic; font-weight: 800; letter-spacing: .5px;
    text-shadow: 0 0 10px var(--violet-bright), 0 0 2px #fff;
  }
  .badge-title--small { top: 196px; font-size: 30px; }
  .badge-title--large { top: 225px; font-size: 39px; }
  .badge-rule {
    position: absolute; left: 220px; top: 276px; width: 140px;
    border-top: 2px dotted var(--ink-soft);
  }
  .badge-date { position: absolute; left: 0; width: 580px; text-align: center; }
  .badge-date--year { top: 283px; font-size: 17px; font-weight: 600; letter-spacing: .5px; }
  .badge-date--day { top: 306px; font-size: 21px; font-weight: 700; }

  .venue-mark {
    position: absolute; left: 388px; top: 368px; width: 124px; text-align: center;
  }
  .venue-mark__dot {
    display: block; width: 42px; height: 42px; margin: 0 auto 8px;
    border-radius: 50%; background: var(--venue-dot);
  }
  .venue-mark__name { font-size: 23px; font-weight: 500; letter-spacing: 1px; color: var(--ink); }

  .address {
    position: absolute; left: 0; width: 564px; top: 474px; text-align: center;
    font-family: "Barlow Semi Condensed", sans-serif; font-weight: 600;
    font-size: 26px; line-height: 32px; text-transform: uppercase;
  }
  .address__rule {
    position: absolute; left: 236px; top: 553px; width: 92px; border-top: 2px solid var(--ink);
  }
  .lineup-main {
    position: absolute; left: 0; width: 564px; top: 580px; text-align: center;
    font-family: "Barlow Semi Condensed", sans-serif; font-weight: 600; font-size: 21px;
  }
  .lineup-residents {
    position: absolute; left: 66px; top: 617px; width: 430px; height: 34px;
  }
  .lineup-residents svg { position: absolute; inset: 0; width: 100%; height: 100%; }
  .lineup-residents span {
    position: absolute; inset: 0; display: flex; align-items: center; justify-content: center;
    font-family: "Barlow Semi Condensed", sans-serif; font-weight: 500; font-size: 14.5px;
  }
  .inquiries {
    position: absolute; left: 0; width: 564px; top: 686px; text-align: center;
    font-weight: 300; font-size: 18px; color: var(--ink-soft);
  }
  .website {
    position: absolute; left: 0; width: 564px; top: 712px; text-align: center;
    font-weight: 500; font-size: 13px; letter-spacing: 3.2px;
  }
</style>
</head>
<body>
  <main class="flyer">
    <svg class="backdrop" viewBox="0 0 552 780">
      <defs>
        <radialGradient id="burst" cx="50%" cy="50%" r="50%">
          <stop offset="55%" stop-color="#8a2be2" stop-opacity=".55"/>
          <stop offset="100%" stop-color="#8a2be2" stop-opacity="0"/>
        </radialGradient>
        <radialGradient id="halftone" cx="50%" cy="50%" r="50%">
          <stop offset="0%" stop-color="#b04ad8" stop-opacity=".5"/>
          <stop offset="100%" stop-color="#b04ad8" stop-opacity="0"/>
        </radialGradient>
        <linearGradient id="blob" x1="0" y1="0" x2="1" y2="1">
          <stop offset="0%" stop-color="#c04ad0" stop-opacity=".55"/>
          <stop offset="100%" stop-color="#5b1a9a" stop-opacity=".2"/>
        </linearGradient>
        <linearGradient id="city" x1="0" y1="0" x2="0" y2="1">
          <stop offset="0%" stop-color="#3a1577" stop-opacity=".6"/>
          <stop offset="100%" stop-color="#2a0f5c" stop-opacity=".9"/>
        </linearGradient>
      </defs>

      <path d="M0 420 C60 400 110 430 100 500 C92 560 60 600 0 610 Z" fill="url(#blob)"/>
      <path d="M490 410 C530 400 552 420 552 430 L552 560 C520 570 480 540 476 500 C472 460 470 420 490 410 Z" fill="url(#blob)"/>
      <path d="M0 470 L170 610" stroke="#b04ad8" stroke-width="2" opacity=".5"/>
      <path d="M20 530 L70 580 L20 630" stroke="#8a4ae0" stroke-width="3" fill="none" opacity=".45"/>
      <path d="M552 430 L380 620" stroke="#6a8ae8" stroke-width="2" opacity=".45"/>

      <ellipse cx="290" cy="250" rx="185" ry="178" fill="url(#burst)" role="img" aria-label="Purple particle wave burst"/>
      <circle cx="88" cy="340" r="48" fill="url(#halftone)" role="img" aria-label="Soft dotted glow"/>
      <circle cx="505" cy="300" r="40" fill="url(#halftone)" role="img" aria-label="Soft dotted glow"/>

      <circle cx="290" cy="250" r="156" fill="none" stroke="#9a4ae8" stroke-width="1" opacity=".7"/>
      <circle cx="290" cy="250" r="138" fill="none" stroke="#7a28d0" stroke-width="14" opacity=".55" role="img" aria-label="Glowing ring band"/>
      <circle cx="290" cy="250" r="120" fill="none" stroke="#a43cff" stroke-width="2" opacity=".7"/>
      <circle cx="290" cy="250" r="106" fill="#1a0b45" stroke="#9b30ff" stroke-width="7"/>

      <path d="M0 780 L0 690 L40 690 L40 665 L80 665 L80 700 L150 700 L150 660 L200 660 L200 690 L240 690 L240 650 L290 650 L290 680 L330 680 L330 640 L380 640 L380 675 L420 675 L420 655 L470 655 L470 690 L520 690 L520 670 L552 670 L552 780 Z" fill="url(#city)" role="img" aria-label="City skyline silhouette"/>
    </svg>

    <div class="level-glow level-glow--top level-glow--left" role="img" aria-label="Colourful sound level glow"></div>
    <div class="level-glow level-glow--top level-glow--right" role="img" aria-label="Colourful sound level glow"></div>
    <div class="level-glow level-glow--bottom level-glow--left" role="img" aria-label="Colourful sound level glow"></div>
    <div class="level-glow level-glow--bottom level-glow--right" role="img" aria-label="Colourful sound level glow"></div>

    <h1 class="event-title">
      <span class="badge-title badge-title--small">HARBOR</span>
      <span class="badge-title badge-title--large">FRIDAYS</span>
    </h1>
    <div class="badge-rule"></div>
    <p class="badge-date badge-date--year">FRI MAY 2020</p>
    <p class="badge-date badge-date--day">1 MAY</p>

    <div class="venue-mark">
      <span class="venue-mark__dot"></span>
      <span class="venue-mark__name">HARBOR</span>
    </div>

    <p class="address">4217 Marlow Avenue<br>Sacramento</p>
    <div class="address__rule"></div>

    <p class="lineup-main">DJ VORTAN (club floor)</p>
    <div class="lineup-residents">
      <svg viewBox="0 0 430 34" preserveAspectRatio="none">
        <path d="M14 1 L416 1 L429 17 L416 33 L14 33 L1 17 Z" fill="rgba(40,10,90,.4)" stroke="#e2552a" stroke-width="2"/>
      </svg>
      <span>DJ RUZO &amp; DJ TAV (RESIDENTS ON THE LOUNGE FLOOR)</span>
    </div>

    <p class="inquiries">list/VIP inquiries</p>
    <p class="website">www.harborvenuehall.example</p>
  </main>
</body>
</html>
```